Business Card Design

I need a card design for Melbourne based business in Australia, called M P Concrete Services. We Concrete and excavate. Concreteing is main part of business.Commercial ,Residential and industrial.We want to be known as M P C (services) as form of abbreviation.We would like to highlight the initials with contact phone. A clean straight edge design. We have no color preference and would prefer a design that can easily be used on all parts of our business including clothing,vechiles and stationary

Industry/Entity Type

Business

Contact Information for Business Card

Hugh 0491 570 156
Peter 0491 570 157
mpcsercices@quollmail.com

```html
<!DOCTYPE html>
<html lang="en">
<head>
<meta charset="utf-8">
<title>M P Concrete Services — Business Card</title>
<link rel="stylesheet" href="https://fonts.googleapis.com/css2?family=Dosis:wght@300;500;600&display=swap">
<style>
  :root {
    --page-bg: #ece8e2;
    --orange-deep: #ee6a0a;
    --orange-bright: #ffa21f;
    --orange-edge: #d85a06;
    --white: #ffffff;
    --truck-yellow: #f2a12a;
    --truck-grey: #8e9296;
    --sky-pale: #dfe4e8;
  }
  * { box-sizing: border-box; margin: 0; padding: 0; }
  html, body {
    width: 1200px; height: 900px; overflow: hidden;
    background: var(--page-bg);
    font-family: "Dosis", sans-serif;
  }
  .sheet {
    position: relative; width: 1200px; height: 900px;
    display: flex; align-items: center; justify-content: center; gap: 60px;
  }
  .card {
    position: relative; width: 500px; height: 306px;
    border-radius: 4px; overflow: hidden;
    box-shadow: 0 10px 28px rgba(0,0,0,0.18);
  }
  /* Front */
  .card-front {
    background: linear-gradient(135deg, var(--orange-deep) 0%, var(--orange-bright) 100%);
    color: var(--white);
  }
  .card-front .top-band {
    position: absolute; top: 0; left: 0; width: 100%; height: 34px;
  }
  .card-front .content {
    position: absolute; left: 44px; top: 66px; right: 30px;
  }
  .wordmark {
    font-weight: 300; font-size: 92px; line-height: 1;
    letter-spacing: 10px; color: var(--white);
  }
  .contact-list {
    list-style: none; margin-top: 22px;
    font-size: 21px; line-height: 1.35; font-weight: 300; letter-spacing: 0.5px;
  }
  .contact-name { font-weight: 600; text-transform: uppercase; margin-right: 10px; }
  .contact-email { font-size: 19px; }
  /* Back */
  .card-back .truck-photo {
    position: absolute; inset: 0;
    background:
      linear-gradient(160deg, var(--sky-pale) 0%, rgba(223,228,232,0) 45%),
      linear-gradient(100deg, var(--truck-grey) 0%, var(--truck-yellow) 45%, var(--orange-deep) 62%, var(--truck-grey) 100%);
  }
</style>
</head>
<body>
  <main class="sheet">
    <section class="card card-front" aria-label="M P Concrete Services business card, front">
      <svg class="top-band" viewBox="0 0 500 34" preserveAspectRatio="none" aria-hidden="true">
        <polygon points="0,0 500,0 500,8 60,8 40,34 0,34" fill="var(--white)" opacity="0.9"/>
        <polygon points="60,8 500,8 500,12 63,12 43,34 40,34" fill="var(--orange-edge)" opacity="0.5"/>
      </svg>
      <div class="content">
        <div class="wordmark">MPC</div>
        <ul class="contact-list">
          <li><span class="contact-name">Hugh</span>0491 570 156</li>
          <li><span class="contact-name">Peter</span>0491 570 157</li>
          <li class="contact-email">mpcsercices@quollmail.com</li>
        </ul>
      </div>
    </section>

    <section class="card card-back" aria-label="M P Concrete Services business card, back">
      <div class="truck-photo" role="img" aria-label="Photograph of orange and yellow concrete mixer trucks parked beside a grey industrial building"></div>
    </section>
  </main>
</body>
</html>
```